Brindle Finance Flyer Design

I would like a high res flyer designed for mass printing. It is for a mortgage and finance broking company in Sydney. We are called Brindle Finance. The wording i would like displayed is the following
Looking For Something Extra from your broker?
Brindle Finance can make all the difference
What we offer you is an extensive range of mortgage and finance products, including:
• Home Loans
• Investment Loans
• Low Doc Loans
• Vehicle Finance
• Equipment Finance
• Commercial Loans
• Refinance
Contact Us
Phone (02) 7412 5830
email info@brindlefinance.com.au
web www.brindlefinance.com.au
Industry/Entity Type
Finance
Look and feel

```html
<!DOCTYPE html>
<html lang="en">
<head>
<meta charset="utf-8">
<title>Brindle Finance Flyer</title>
<link rel="stylesheet" href="https://fonts.googleapis.com/css2?family=Ubuntu:wght@300;400;500;700&display=swap">
<style>
  :root {
    --page-bg: #b9b9b9;
    --paper: #ffffff;
    --ink: #3a3a3a;
    --sand: #ead8b0;
    --sand-text: #ecd6a6;
    --charcoal: #3e3e3e;
    --charcoal-deep: #2f2f2f;
    --photo-light: #eef4f8;
    --photo-mid: #c9d9e6;
    --photo-navy: #2a3b6e;
  }
  * { box-sizing: border-box; margin: 0; padding: 0; }
  html, body { width: 1200px; height: 1200px; overflow: hidden; }
  body {
    background: var(--page-bg);
    font-family: "Ubuntu", sans-serif;
    color: var(--ink);
  }
  .flyer {
    position: absolute;
    left: 190px; top: 20px;
    width: 820px; height: 1160px;
    background: var(--paper);
    overflow: hidden;
  }
  .masthead {
    height: 182px;
    display: flex;
    flex-direction: column;
    align-items: center;
    justify-content: center;
    border-bottom: 2px solid #e6e6e6;
  }
  .brand-row { display: flex; align-items: center; gap: 16px; }
  .brand-square { width: 36px; height: 36px; background: var(--ink); }
  .brand-name {
    font-weight: 400;
    font-size: 62px;
    line-height: 1;
    color: var(--ink);
    letter-spacing: -0.5px;
  }
  .brand-tagline {
    margin-top: 6px;
    margin-left: 52px;
    font-size: 20px;
    font-weight: 400;
    color: var(--ink);
  }
  .hero {
    position: absolute;
    top: 182px; left: 0;
    width: 820px; height: 540px;
    background:
      linear-gradient(90deg, rgba(255,255,255,0) 55%, var(--photo-navy) 70%, #3b4f88 88%, var(--photo-mid) 100%),
      radial-gradient(ellipse at 40% 60%, #ffffff 0%, var(--photo-light) 45%, var(--photo-mid) 100%);
  }
  .headline { position: absolute; top: 239px; left: 40px; }
  .headline-line {
    display: block;
    width: fit-content;
    background: var(--sand);
    height: 67px;
    line-height: 67px;
    padding: 0 28px;
    margin-bottom: 1px;
    font-size: 35px;
    font-weight: 400;
    color: var(--ink);
  }
  .difference-band {
    position: absolute;
    top: 722px; left: 0;
    width: 820px; height: 92px;
    background: var(--sand);
    display: flex; align-items: center; justify-content: center;
    font-size: 29px;
    font-weight: 500;
    letter-spacing: 0.3px;
    color: #2e2e2e;
  }
  .offer {
    position: absolute;
    top: 814px; left: 0;
    width: 820px; height: 245px;
    background: var(--charcoal);
    text-align: center;
    color: var(--sand-text);
  }
  .offer-intro {
    margin: 58px auto 0;
    width: 660px;
    font-size: 24px;
    font-weight: 300;
    line-height: 1.25;
  }
  .product-list {
    margin: 32px auto 0;
    width: 700px;
    list-style: none;
    display: flex; flex-wrap: wrap; justify-content: center;
    font-size: 17px; font-weight: 500; line-height: 26px;
  }
  .product-list li + li::before { content: "•"; margin: 0 13px; }
  .product-list li.row-start::before { content: none; }
  .product-list .break { flex-basis: 100%; height: 0; }
  .contact-bar {
    position: absolute;
    top: 1059px; left: 0;
    width: 820px; height: 101px;
    background: var(--charcoal-deep);
    display: flex; align-items: center; justify-content: center;
    color: var(--sand-text);
    font-size: 18px; font-weight: 300; letter-spacing: 0.6px;
  }
  .contact-sep { margin: 0 26px; }
</style>
</head>
<body>
  <main class="flyer">
    <header class="masthead">
      <div class="brand-row">
        <span class="brand-square"></span>
        <span class="brand-name">Brindle Finance</span>
      </div>
      <p class="brand-tagline">mortgage and finance broking services</p>
    </header>

    <div class="hero" role="img" aria-label="Blurred photo of business people walking through a bright office corridor"></div>

    <h1 class="headline">
      <span class="headline-line">Looking For Something</span>
      <span class="headline-line">Extra from your</span>
      <span class="headline-line">broker?</span>
    </h1>

    <div class="difference-band">BRINDLE FINANCE CAN MAKE ALL THE DIFFERENCE</div>

    <section class="offer">
      <p class="offer-intro">What we offer you is an extensive range of mortgage and finance products, including:</p>
      <ul class="product-list">
        <li class="row-start">Home Loans</li>
        <li>Investment Loans</li>
        <li>Low Doc Loans</li>
        <li>Vehicle Finance</li>
        <li class="break" aria-hidden="true"></li>
        <li class="row-start">Equipment Finance</li>
        <li>Commercial Loans</li>
        <li>Refinance</li>
      </ul>
    </section>

    <footer class="contact-bar">
      <span class="contact-phone">(02) 7412 5830</span>
      <span class="contact-sep">|</span>
      <span class="contact-email">info@brindlefinance.com.au</span>
      <span class="contact-sep">|</span>
      <span class="contact-web">www.brindlefinance.com.au</span>
    </footer>
  </main>
</body>
</html>
```